Sales PowerPoint Template to help us attract new customers

We need to create a generic PowerPoint template for our organization. We are in the commercial facilities industry, servicing convenience, restaurants, grocery, and retail customers in the US. We handle trades such as HVAC, Refrigeration, Plumbing, Electrical, Food Equipment, Coffee, etc.

We need to incorporate our new logo, updated colors, Font (Arial). We want it to stand out in this deck and avoid looking like all other facility companies. We want to make sure the template size is not too large (less than 20 MB), so it prevent people to edit/send.
Attached are new logo, colors, old powerpoint template, and finally the "New Design to Incorporate into Template" is new materials we're looking to leverage. This might give you ideas.

Create at least 10 slides (1 cover, 1 agenda slide, at least 7 general slides, and 1 wrap-up slide)

Target Market(s)

Convenience Stores, Retail Stores, Groceries, and Restaurants in the US

Industry/Entity Type

Facilities Services (HVAC, Refrigeration, Plumbing, Electrical, etc, repair and preventative maintenance)

Font styles to use
Other font styles liked:
• Arial

Requirements
Must have
• Follow company colors and font (Arial)
Should not have
• Not approved company colors, font

```html
<!DOCTYPE html>
<html lang="en">
<head>
<meta charset="utf-8">
<title>Norvex Sales Deck Template</title>
<link rel="stylesheet" href="https://fonts.googleapis.com/css2?family=Arimo:wght@400;700&display=swap">
<style>
  :root {
    --night: #1b1c3d;
    --white: #ffffff;
    --olive: #8c9a2e;
    --navy: #22386b;
    --orange: #f0a11c;
    --teal: #2b8c9b;
    --brown: #8a5a2b;
    --charcoal: #343434;
    --ink: #222222;
    --mist: #e7ebef;
    --line: #d4d8dc;
  }
  * { margin: 0; padding: 0; box-sizing: border-box; }
  html, body { width: 753px; height: 1200px; overflow: hidden; }
  body {
    background: var(--night);
    font-family: "Arimo", Arial, sans-serif;
    color: var(--ink);
    position: relative;
  }
  .slide {
    position: absolute;
    left: 107px;
    width: 540px;
    height: 304px;
    background: var(--white);
    overflow: hidden;
  }
  .slide--cover { top: 100px; }
  .slide--steps { top: 451px; }
  .slide--data { top: 798px; }

  .brand { position: absolute; left: 24px; top: 18px; display: flex; align-items: flex-start; gap: 6px; }
  .brand__dot { width: 10px; height: 10px; background: var(--olive); margin-top: 4px; }
  .brand__name { font-weight: 700; font-size: 16px; letter-spacing: 3px; color: var(--charcoal); line-height: 1; }
  .brand__tag { font-size: 8px; color: var(--olive); margin-top: 3px; }

  .footer { position: absolute; left: 0; right: 0; bottom: 0; height: 24px; }
  .footer__bar {
    position: absolute; left: 0; bottom: 6px; width: 150px; height: 20px;
    background: var(--olive); border-radius: 0 12px 12px 0;
    color: var(--white); font-size: 8px; font-weight: 700; line-height: 20px; padding-left: 14px;
  }
  .footer__navy { position: absolute; left: 150px; right: 0; bottom: 6px; height: 3px; background: var(--navy); }
  .footer__orange { position: absolute; left: 300px; width: 120px; bottom: 6px; height: 3px; background: var(--orange); }

  .photo { position: absolute; }
  .photo--technician {
    right: 0; top: 0; width: 250px; height: 276px;
    background: linear-gradient(160deg, #b9c7d3 0%, #8796a4 45%, #5f6b76 100%);
    clip-path: polygon(18% 0, 100% 0, 100% 100%, 55% 100%, 0 30%);
  }
  .cover__shard { position: absolute; right: 0; bottom: 0; }
  .cover__meta { position: absolute; left: 24px; top: 70px; font-size: 7px; color: var(--charcoal); }
  .cover__title { position: absolute; left: 24px; top: 90px; font-size: 20px; font-weight: 700; color: var(--olive); }
  .cover__rule { position: absolute; left: 24px; top: 116px; width: 60px; height: 3px; background: var(--orange); }
  .cover__subtitle { position: absolute; left: 24px; top: 128px; font-size: 14px; font-weight: 700; color: var(--ink); }

  .photo--wash {
    left: 0; top: 0; width: 330px; height: 140px;
    background: linear-gradient(180deg, #dde2e7 0%, #f4f5f7 100%);
    opacity: .8;
  }
  .photo--gauges {
    right: 0; bottom: 24px; width: 170px; height: 160px;
    background: linear-gradient(150deg, #c95a3d 0%, #3f6fa8 55%, #2b3440 100%);
    clip-path: polygon(100% 0, 100% 100%, 0 100%);
  }
  .step { position: absolute; display: flex; align-items: center; gap: 10px; }
  .step__mark { position: relative; width: 36px; height: 32px; }
  .step__mark svg { position: absolute; inset: 0; }
  .step__num { position: absolute; left: 0; right: 0; top: 3px; text-align: center; color: var(--white); font-weight: 700; font-size: 15px; }
  .step__text { font-size: 10px; line-height: 1.25; color: var(--ink); }

  .data__title { position: absolute; left: 24px; top: 54px; font-size: 20px; font-weight: 700; color: var(--olive); }
  .data__subtitle { position: absolute; left: 24px; top: 80px; font-size: 12px; font-weight: 700; color: var(--ink); }
  .table { position: absolute; left: 28px; top: 122px; width: 180px; border-collapse: collapse; font-size: 5px; }
  .table th { color: var(--white); font-weight: 700; padding: 2px 3px; text-align: left; }
  .table th:nth-child(1) { background: var(--navy); }
  .table th:nth-child(2) { background: var(--orange); }
  .table th:nth-child(3) { background: var(--teal); }
  .table td { padding: 2px 3px; border-bottom: 1px solid var(--line); color: var(--charcoal); }
  .table tr:nth-child(even) td { background: var(--mist); }
  .donut { position: absolute; left: 238px; top: 100px; }
  .photo--produce {
    right: 0; top: 0; width: 190px; height: 280px;
    background: linear-gradient(170deg, #6b8a3a 0%, #b83a2a 45%, #8a2a1f 75%, #4a5a2a 100%);
    clip-path: polygon(32% 0, 100% 0, 100% 100%, 0 100%, 18% 35%);
  }
</style>
</head>
<body>

<section class="slide slide--cover">
  <div class="photo photo--technician" role="img" aria-label="Photo of a technician servicing rooftop HVAC equipment"></div>
  <svg class="cover__shard" width="200" height="110" viewBox="0 0 200 110" aria-hidden="true">
    <polygon points="200,0 200,110 60,110" fill="#ffffff"/>
    <polygon points="200,40 200,110 130,110" fill="#e7ebef"/>
  </svg>
  <div class="brand">
    <span class="brand__dot"></span>
    <div><div class="brand__name">NORVEX</div><div class="brand__tag">Facility Solutions</div></div>
  </div>
  <p class="cover__meta">5/12/2020 &nbsp;—&nbsp; Speaker</p>
  <h1 class="cover__title">PRESENTATION TITLE</h1>
  <div class="cover__rule"></div>
  <p class="cover__subtitle">Enter your subtitle here</p>
  <div class="footer">
    <div class="footer__navy"></div><div class="footer__orange"></div>
    <div class="footer__bar">www.norvex.com</div>
  </div>
</section>

<section class="slide slide--steps">
  <div class="photo photo--wash" role="img" aria-label="Faded photo of a facility service scene"></div>
  <div class="photo photo--gauges" role="img" aria-label="Photo of refrigeration gauges being connected"></div>
  <div class="brand">
    <span class="brand__dot"></span>
    <div><div class="brand__name">NORVEX</div><div class="brand__tag">Facility Solutions</div></div>
  </div>

  <div class="step" style="left:58px;top:66px">
    <div class="step__mark"><svg width="36" height="32" viewBox="0 0 36 32"><polygon points="0,0 36,0 18,32" fill="var(--olive)"/></svg><span class="step__num">1</span></div>
    <p class="step__text">This is a<br>placeholder text.</p>
  </div>
  <div class="step" style="left:245px;top:66px">
    <div class="step__mark"><svg width="36" height="32" viewBox="0 0 36 32"><polygon points="0,0 36,0 18,32" fill="var(--charcoal)"/></svg><span class="step__num">2</span></div>
    <p class="step__text">This is a<br>placeholder text.</p>
  </div>
  <div class="step" style="left:58px;top:142px">
    <div class="step__mark"><svg width="36" height="32" viewBox="0 0 36 32"><polygon points="0,0 36,0 18,32" fill="var(--teal)"/></svg><span class="step__num">3</span></div>
    <p class="step__text">This is a<br>placeholder text.</p>
  </div>
  <div class="step" style="left:245px;top:142px">
    <div class="step__mark"><svg width="36" height="32" viewBox="0 0 36 32"><polygon points="0,0 36,0 18,32" fill="var(--orange)"/></svg><span class="step__num">4</span></div>
    <p class="step__text">This is a<br>placeholder text.</p>
  </div>
  <div class="step" style="left:58px;top:216px">
    <div class="step__mark"><svg width="36" height="32" viewBox="0 0 36 32"><polygon points="0,0 36,0 18,32" fill="var(--brown)"/></svg><span class="step__num">5</span></div>
    <p class="step__text">This is a<br>placeholder text.</p>
  </div>
  <div class="step" style="left:245px;top:216px">
    <div class="step__mark"><svg width="36" height="32" viewBox="0 0 36 32"><polygon points="0,0 36,0 18,32" fill="var(--navy)"/></svg><span class="step__num">6</span></div>
    <p class="step__text">This is a<br>placeholder text.</p>
  </div>

  <div class="footer">
    <div class="footer__navy"></div><div class="footer__orange"></div>
    <div class="footer__bar">www.norvex.com</div>
  </div>
</section>

<section class="slide slide--data">
  <div class="photo photo--produce" role="img" aria-label="Photo of fresh produce on grocery shelves"></div>
  <div class="brand">
    <span class="brand__dot"></span>
    <div><div class="brand__name">NORVEX</div><div class="brand__tag">Facility Solutions</div></div>
  </div>
  <h2 class="data__title">TABLES AND DIAGRAMS</h2>
  <p class="data__subtitle">Enter your subtitle here</p>

  <table class="table">
    <thead><tr><th>Description 1</th><th>Description 2</th><th>Description 3</th><th style="background:var(--olive)">&nbsp;</th></tr></thead>
    <tbody>
      <tr><td>Placeholder text</td><td>xx</td><td>xx</td><td>xx</td></tr>
      <tr><td>Placeholder text</td><td>xx</td><td>xx</td><td>xx</td></tr>
      <tr><td>Placeholder text</td><td>xx</td><td>xx</td><td>xx</td></tr>
      <tr><td>Placeholder text</td><td>xx</td><td>xx</td><td>xx</td></tr>
      <tr><td>Placeholder text</td><td>xx</td><td>xx</td><td>xx</td></tr>
      <tr><td>Placeholder text</td><td>xx</td><td>xx</td><td>xx</td></tr>
      <tr><td>Placeholder text</td><td>xx</td><td>xx</td><td>xx</td></tr>
      <tr><td>Placeholder text</td><td>xx</td><td>xx</td><td>xx</td></tr>
      <tr><td>Placeholder text</td><td>xx</td><td>xx</td><td>xx</td></tr>
    </tbody>
  </table>

  <svg class="donut" width="136" height="136" viewBox="0 0 136 136" role="img" aria-label="Donut chart">
    <g transform="rotate(-90 68 68)" fill="none" stroke-width="26">
      <circle cx="68" cy="68" r="52" stroke="var(--teal)" stroke-dasharray="147 180" stroke-dashoffset="0"/>
      <circle cx="68" cy="68" r="52" stroke="var(--navy)" stroke-dasharray="65 262" stroke-dashoffset="-147"/>
      <circle cx="68" cy="68" r="52" stroke="var(--brown)" stroke-dasharray="49 278" stroke-dashoffset="-212"/>
      <circle cx="68" cy="68" r="52" stroke="var(--orange)" stroke-dasharray="33 294" stroke-dashoffset="-261"/>
      <circle cx="68" cy="68" r="52" stroke="var(--olive)" stroke-dasharray="33 294" stroke-dashoffset="-294"/>
    </g>
  </svg>

  <div class="footer">
    <div class="footer__navy"></div><div class="footer__orange"></div>
    <div class="footer__bar">www.norvex.com</div>
  </div>
</section>

</body>
</html>
```